Still Brook Trail - Business Card

May try various combos of colors from primary & secondary palette attached below. Logo and Catch phrase previous built logo attached should go on front, but change to color palette options noted. may try various color options from minimal to zen like quality/vibe.
On Front: Attached Logo & Phrase
On Back:
https://stillbrooktrail.com/
415.283.7904
stillbrooktrail@openlanterndesk.ai

Contact Information for Business Card

Daniel R. Forsyth, MD Founder & CEO https://stillbrooktrail.com/ 415.283.7904 stillbrooktrail@openlanterndesk.ai

```html
<!DOCTYPE html>
<html lang="en">
<head>
<meta charset="utf-8">
<title>Still Brook Trail – Business Card</title>
<link href="https://fonts.googleapis.com/css2?family=Montserrat:wght@400;500;700&family=Tinos&display=swap" rel="stylesheet">
<style>
  :root {
    --bg: #d3d3d3;
    --paper: #f1f1ee;
    --green: #2f5a22;
    --grey: #8a8a8a;
    --text-grey: #6b6b6b;
    --icon-red: #c8322b;
    --icon-orange: #e07a3a;
  }
  * { margin: 0; padding: 0; box-sizing: border-box; }
  html, body { width: 1200px; height: 1051px; overflow: hidden; }
  body {
    background: var(--bg);
    font-family: "Montserrat", sans-serif;
    display: flex;
    flex-direction: column;
    align-items: center;
    justify-content: center;
    gap: 60px;
  }
  .card {
    width: 560px;
    height: 320px;
    background: var(--paper);
    border-bottom: 4px solid var(--green);
    box-shadow: 0 6px 18px rgba(0,0,0,0.12);
    position: relative;
  }
  .lockup {
    display: flex;
    flex-direction: column;
    align-items: center;
  }
  .lockup-row { display: flex; align-items: center; }
  .lockup-mark {
    border: 2px solid var(--green);
    border-radius: 50%;
    flex: none;
  }
  .lockup-name {
    font-family: "Tinos", serif;
    color: var(--green);
    font-weight: 400;
    white-space: nowrap;
    line-height: 1;
  }
  .lockup-tagline {
    color: var(--grey);
    font-weight: 400;
    white-space: nowrap;
  }
  /* front */
  .card-front { display: flex; align-items: center; justify-content: center; }
  .card-front .lockup { gap: 10px; }
  .card-front .lockup-row { gap: 14px; }
  .card-front .lockup-mark { width: 54px; height: 54px; }
  .card-front .lockup-name { font-size: 42px; }
  .card-front .lockup-tagline { font-size: 13px; }
  /* back */
  .card-back { display: flex; align-items: center; justify-content: space-between; padding: 0 34px; }
  .contact { display: flex; flex-direction: column; gap: 5px; }
  .contact-name { color: var(--green); font-weight: 700; font-size: 17px; }
  .contact-name .suffix { font-weight: 500; }
  .contact-role { color: var(--text-grey); font-size: 12px; margin-bottom: 8px; }
  .contact-line { display: flex; align-items: center; gap: 7px; color: var(--text-grey); font-size: 11.5px; }
  .contact-line svg { width: 11px; height: 11px; flex: none; }
  .card-back .lockup { gap: 6px; }
  .card-back .lockup-row { gap: 9px; }
  .card-back .lockup-mark { width: 30px; height: 30px; }
  .card-back .lockup-name { font-size: 24px; }
  .card-back .lockup-tagline { font-size: 8px; }
</style>
</head>
<body>
  <section class="card card-front">
    <div class="lockup">
      <div class="lockup-row">
        <span class="lockup-mark"></span>
        <span class="lockup-name">Still Brook Trail</span>
      </div>
      <span class="lockup-tagline">Nurturing Calm Minds, Bodies &amp; Hearts</span>
    </div>
  </section>

  <section class="card card-back">
    <div class="contact">
      <p class="contact-name">Daniel R. Forsyth, <span class="suffix">MD</span></p>
      <p class="contact-role">Founder &amp; CEO</p>
      <p class="contact-line">
        <svg viewBox="0 0 12 12"><path fill="var(--green)" d="M2.5 1l2 2-1 1.3c.6 1.4 1.8 2.6 3.2 3.2L8 6.5l2 2-1.2 1.8C5 10 2 7 1.7 3.2z"/></svg>
        415.283.7904
      </p>
      <p class="contact-line">
        <svg viewBox="0 0 12 12"><rect x="1" y="2.5" width="10" height="7" fill="var(--icon-red)"/><path d="M1 2.5l5 4 5-4" stroke="#fff" stroke-width="1" fill="none"/></svg>
        stillbrooktrail@openlanterndesk.ai
      </p>
      <p class="contact-line">
        <svg viewBox="0 0 12 12"><circle cx="6" cy="6" r="5" fill="var(--icon-orange)"/><path d="M1 6h10M6 1c-2 2.5-2 7.5 0 10M6 1c2 2.5 2 7.5 0 10" stroke="#fff" stroke-width=".8" fill="none"/></svg>
        stillbrooktrail.com
      </p>
    </div>
    <div class="lockup">
      <div class="lockup-row">
        <span class="lockup-mark"></span>
        <span class="lockup-name">Still Brook Trail</span>
      </div>
      <span class="lockup-tagline">Nurturing Calm Minds, Bodies &amp; Hearts</span>
    </div>
  </section>
</body>
</html>
```